Dunmore Air & Co business card

I need an awesome, double-sided business card designed with our new logo. I would like the one side black with the colored logo, and the back side is all yours. I'd like to see horizontal and vertical layouts. Get creative! Thank you.

Target Market(s)

HVAC, Heating and Cooling in Phoenix, AZ

Industry/Entity Type

HVAC

Contact Information for Business Card

We need our new logo on the card. Tom Harker, (623) 417-2958, tom@brightvaleair.com, www.brightvaleair.com, ROC 581427

```html
<!DOCTYPE html>
<html lang="en">
<head>
<meta charset="utf-8">
<title>Dunmore Air &amp; Co — Business Card</title>
<link rel="stylesheet" href="https://fonts.googleapis.com/css2?family=Roboto:wght@400&family=Roboto+Condensed:wght@700&display=swap">
<style>
  :root {
    --backdrop: #2b2b2b;
    --card: #f1f1f1;
    --blue: #0b4fa6;
    --blue-light: #1583de;
    --orange: #ee8a1f;
    --red: #d9321f;
    --ink: #1e1e1e;
    --white: #ffffff;
  }
  * { margin: 0; padding: 0; box-sizing: border-box; }
  html, body { width: 1200px; height: 1138px; overflow: hidden; }
  body { background: var(--backdrop); position: relative; font-family: "Roboto", sans-serif; }

  .card {
    position: absolute;
    width: 620px;
    height: 376px;
    background: var(--card);
    border-radius: 14px;
    overflow: hidden;
  }
  .card--front { left: 272px; top: 184px; }
  .card--back  { left: 274px; top: 606px; }

  .brand {
    position: absolute;
    display: flex;
    align-items: center;
    gap: 10px;
    transform: translate(-50%, -50%);
    white-space: nowrap;
  }
  .brand__dot { width: 22px; height: 22px; border-radius: 50%; background: var(--orange); }
  .brand__name {
    font-family: "Roboto Condensed", sans-serif;
    font-weight: 700;
    color: var(--blue);
    font-size: 40px;
    letter-spacing: 0.5px;
  }
  .card--front .brand { left: 312px; top: 176px; }
  .card--back .brand { left: 166px; top: 182px; }
  .card--back .brand__name { font-size: 34px; }
  .card--back .brand__dot { width: 18px; height: 18px; }

  .edge-stripe { position: absolute; left: 0; bottom: 0; width: 100%; height: 12px; display: flex; }
  .edge-stripe__blue { flex: 1; background: var(--blue); }
  .edge-stripe__orange { flex: 1; background: linear-gradient(90deg, var(--orange), var(--red)); }

  .wave { position: absolute; left: 0; top: 0; width: 620px; height: 200px; }

  .holder-name {
    position: absolute;
    right: 41px;
    top: 40px;
    font-family: "Roboto Condensed", sans-serif;
    font-weight: 700;
    font-size: 25px;
    color: var(--white);
    letter-spacing: 0.3px;
  }

  .contact { position: absolute; right: 40px; top: 270px; list-style: none; }
  .contact__item {
    display: flex; align-items: center; justify-content: flex-end; gap: 9px;
    font-size: 16px; color: var(--ink); height: 24px;
  }
  .contact__icon { width: 14px; height: 14px; }

  .licence { position: absolute; left: 42px; top: 318px; font-size: 16px; color: var(--ink); }
</style>
</head>
<body>

<section class="card card--front">
  <div class="brand">
    <span class="brand__dot"></span>
    <span class="brand__name">Dunmore Air &amp; Co</span>
  </div>
  <div class="edge-stripe">
    <span class="edge-stripe__blue"></span>
    <span class="edge-stripe__orange"></span>
  </div>
</section>

<section class="card card--back">
  <svg class="wave" viewBox="0 0 620 200" aria-hidden="true">
    <defs>
      <linearGradient id="waveBlue" x1="0" y1="0" x2="1" y2="1">
        <stop offset="0" stop-color="#1583de"/>
        <stop offset="0.5" stop-color="#0b4fa6"/>
        <stop offset="1" stop-color="#0a3f8a"/>
      </linearGradient>
      <linearGradient id="waveOrange" x1="0" y1="0" x2="1" y2="0">
        <stop offset="0" stop-color="#ee8a1f"/>
        <stop offset="0.6" stop-color="#e4551e"/>
        <stop offset="1" stop-color="#d9321f"/>
      </linearGradient>
    </defs>
    <path fill="url(#waveBlue)" d="M0,0 H620 V120 C545,145 470,142 400,108 C320,68 250,18 150,18 C80,18 30,35 0,50 Z"/>
    <path fill="url(#waveOrange)" d="M0,58 C40,38 90,28 150,28 C250,28 320,78 395,118 C470,156 545,158 620,132 V146 C540,175 460,170 385,132 C315,96 240,52 150,52 C85,52 35,68 0,86 Z"/>
  </svg>

  <h1 class="holder-name">TOM HARKER</h1>

  <div class="brand">
    <span class="brand__dot"></span>
    <span class="brand__name">Dunmore Air &amp; Co</span>
  </div>

  <ul class="contact">
    <li class="contact__item">(623) 417-2958
      <svg class="contact__icon" viewBox="0 0 14 14" aria-hidden="true"><path fill="#d9321f" d="M1,5 C1,2 13,2 13,5 V6 H10 V4.5 H4 V6 H1 Z M3,7 H11 L12,12 H2 Z"/></svg>
    </li>
    <li class="contact__item">tom@brightvaleair.com
      <svg class="contact__icon" viewBox="0 0 14 14" aria-hidden="true"><rect x="1" y="3" width="12" height="8" fill="#d9321f"/><path d="M1,3 L7,8 L13,3" stroke="#fff" stroke-width="1.2" fill="none"/></svg>
    </li>
    <li class="contact__item">www.brightvaleair.com
      <svg class="contact__icon" viewBox="0 0 14 14" aria-hidden="true"><circle cx="7" cy="7" r="6" fill="#e4551e"/><path d="M1,7 H13 M7,1 V13 M2.5,4 H11.5 M2.5,10 H11.5" stroke="#fff" stroke-width="0.8" fill="none"/><ellipse cx="7" cy="7" rx="2.6" ry="6" stroke="#fff" stroke-width="0.8" fill="none"/></svg>
    </li>
  </ul>

  <p class="licence">ROC 581427</p>
</section>

</body>
</html>
```